Sandwich Board and Poster design promoting a medical aesthetic clinic

I am looking for a clean, modern and relaxing design promoting a medical physician-led aesthetic clinic.
Services offered are neuromodulator treatment (Quelvo) and Dermal Fillers.
Logo must be included.
Use the tag line "Refresh your look, revive your spirit."
Address is 204-205 27361 92 Ave, Surrey, V7K 2M4
604-555-0148
email - info@lumawellpine.ca
www.lumawellpine.ca

```html
<!DOCTYPE html>
<html lang="en">
<head>
<meta charset="utf-8">
<title>Lumawell Pine – Refresh Your Look</title>
<link rel="stylesheet" href="https://fonts.googleapis.com/css2?family=Oswald:wght@600&family=Roboto+Condensed:wght@400;700&family=Poppins:wght@400;500&display=swap">
<style>
  :root {
    --backdrop: #b4b4b4;
    --paper: #f1f2f5;
    --ink: #1a1a1a;
    --headline: #231815;
    --gold: #dcb62a;
    --navy: #1c3057;
    --white: #ffffff;
  }
  * { margin: 0; padding: 0; box-sizing: border-box; }
  html, body { width: 1200px; height: 1200px; overflow: hidden; background: var(--backdrop); }
  .poster {
    position: absolute; left: 182px; top: 11px; width: 836px; height: 1178px;
    background: radial-gradient(ellipse at 55% 55%, #fbfbfd 0%, var(--paper) 70%);
    overflow: hidden;
  }
  .brand {
    position: absolute; top: 128px; left: 0; width: 100%; text-align: center;
    font-family: "Poppins", sans-serif; font-weight: 500; font-size: 28px;
    letter-spacing: 0.3em; color: var(--ink); padding-left: 0.3em;
  }
  .hero-photo {
    position: absolute; left: 35px; top: 218px; width: 237px; height: 576px;
    border-radius: 150px 0 0 60px;
    background: linear-gradient(160deg, #d9c29a 0%, #e8c9b2 40%, #f0d6c6 75%, #efe7e2 100%);
  }
  .headline { position: absolute; left: 0; top: 0; width: 836px; height: 820px; }
  .headline text { font-family: "Oswald", sans-serif; font-weight: 600; fill: var(--headline); }
  .gold-band { position: absolute; left: 0; top: 941px; width: 100%; height: 237px; background: var(--gold); }
  .service-photo {
    position: absolute; top: 830px; width: 226px; height: 226px; border-radius: 50%;
    border: 7px solid var(--white);
  }
  .service-photo--left { left: 49px; background: linear-gradient(135deg, #bfe3ee 0%, #b98a6c 50%, #4a2f24 100%); }
  .service-photo--right { left: 568px; background: linear-gradient(135deg, #3f59b5 0%, #c69577 55%, #6e4a3a 100%); }
  .services-badge {
    position: absolute; left: 311px; top: 830px; width: 226px; height: 226px; border-radius: 50%;
    background: var(--white); border: 7px solid var(--gold);
    display: flex; flex-direction: column; align-items: center; justify-content: center;
    font-family: "Roboto Condensed", sans-serif; color: var(--navy); text-align: center; line-height: 1.2;
  }
  .services-badge .intro { font-size: 21px; font-weight: 400; }
  .services-badge .list { font-size: 25px; font-weight: 700; line-height: 1.12; margin-top: 2px; }
  .contacts { position: absolute; left: 0; top: 1104px; width: 100%; height: 50px; }
  .contact { position: absolute; display: flex; align-items: center; gap: 14px; }
  .contact svg { width: 30px; height: 30px; flex: none; }
  .contact p {
    font-family: "Poppins", sans-serif; font-size: 17px; line-height: 22px; color: var(--white);
  }
  .contact--address { left: 55px; }
  .contact--phone { left: 344px; }
  .contact--web { left: 556px; }
</style>
</head>
<body>
<main class="poster">
  <div class="brand">LUMAWELL PINE</div>

  <div class="hero-photo" role="img" aria-label="Photo of a woman in profile with blonde hair"></div>

  <svg class="headline" viewBox="0 0 836 820" aria-label="Refresh your look, revive your spirit">
    <text x="284" y="319" font-size="138" textLength="320" lengthAdjust="spacingAndGlyphs">REFRESH</text>
    <text x="284" y="433" font-size="134" textLength="416" lengthAdjust="spacingAndGlyphs">YOUR LOOK</text>
    <text x="284" y="549" font-size="136" textLength="476" lengthAdjust="spacingAndGlyphs">REVIVE YOUR</text>
    <text x="287" y="784" font-size="290" textLength="514" lengthAdjust="spacingAndGlyphs">SPIRIT</text>
  </svg>

  <div class="gold-band"></div>

  <div class="service-photo service-photo--left" role="img" aria-label="Photo of a woman receiving a forehead injection"></div>
  <div class="services-badge">
    <span class="intro">SERVICES</span>
    <span class="intro">OFFERED ARE</span>
    <span class="list">Neuromodulator<br>Treatment (Quelvo)<br>&amp; Dermal Fillers.</span>
  </div>
  <div class="service-photo service-photo--right" role="img" aria-label="Photo of gloved hands giving a brow injection"></div>

  <section class="contacts">
    <div class="contact contact--address">
      <svg viewBox="0 0 30 30"><circle cx="15" cy="15" r="15" fill="#fff"/><path d="M15 7.5a5 5 0 0 0-5 5c0 3.8 5 9.5 5 9.5s5-5.7 5-9.5a5 5 0 0 0-5-5z" fill="#1c3057"/><circle cx="15" cy="12.5" r="1.9" fill="#fff"/></svg>
      <p>204-205 27361 92 AVE,<br>SURREY, V7K 2M4</p>
    </div>
    <div class="contact contact--phone">
      <svg viewBox="0 0 30 30"><circle cx="15" cy="15" r="15" fill="#fff"/><path d="M11.5 8.5l2.2-.4 1.2 3.3-1.6 1.1c.6 1.7 1.7 3 3.2 3.9l1.3-1.4 3.1 1.6-.5 2.2c-5.2.6-9.6-5.1-8.9-10.3z" fill="#1c3057"/></svg>
      <p>CALL US:<br>604-555-0148</p>
    </div>
    <div class="contact contact--web">
      <svg viewBox="0 0 30 30"><circle cx="15" cy="15" r="15" fill="#fff"/><g fill="none" stroke="#1c3057" stroke-width="1.6"><circle cx="15" cy="15" r="7.5"/><ellipse cx="15" cy="15" rx="3.2" ry="7.5"/><path d="M7.5 15h15M8.5 11h13M8.5 19h13"/></g></svg>
      <p>info@lumawellpine.ca<br>www.lumawellpine.ca</p>
    </div>
  </section>
</main>
</body>
</html>
```